Shaker Barons business card

We would like a business card designed for our business shaker barons

We need it to have 2 sides.

More information about the business can be found at www.shakerbarons.net

```html
<!DOCTYPE html>
<html lang="en">
<head>
<meta charset="UTF-8">
<title>Shaker Barons business card</title>
<link href="https://fonts.googleapis.com/css2?family=Montserrat:wght@400;500;700&display=swap" rel="stylesheet">
<style>
  :root {
    --backdrop: #e9e6e1;
    --card-white: #ffffff;
    --card-black: #111111;
    --ink: #141414;
    --gold: #e4d6ad;
    --band-text: #f2f2f2;
  }
  * { margin: 0; padding: 0; box-sizing: border-box; }
  html, body { width: 1200px; height: 885px; overflow: hidden; }
  body {
    background: var(--backdrop);
    font-family: "Montserrat", sans-serif;
    position: relative;
  }
  .card {
    position: absolute;
    top: 145px;
    width: 340px;
    height: 595px;
    border-radius: 4px;
    overflow: hidden;
    box-shadow: 0 10px 28px rgba(0,0,0,0.22);
  }
  .card-front { left: 230px; background: var(--card-white); color: var(--ink); }
  .card-back { left: 630px; background: var(--card-black); }

  .front-brand {
    position: absolute;
    top: 70px; left: 0; right: 0;
    text-align: center;
    font-size: 34px;
    font-weight: 700;
    letter-spacing: 0.5px;
  }
  .front-person {
    position: absolute;
    top: 178px; left: 0; right: 0;
    text-align: center;
  }
  .person-name { font-size: 28px; font-weight: 700; line-height: 1.1; }
  .person-role { font-size: 20px; font-weight: 500; }

  .front-contacts {
    position: absolute;
    top: 300px; left: 0; right: 0;
    text-align: center;
    font-size: 19px;
    font-weight: 500;
    line-height: 1.3;
    letter-spacing: 0.3px;
  }
  .front-band {
    position: absolute;
    left: 0; right: 0; bottom: 0;
    height: 92px;
    background: var(--card-black);
    display: flex;
    align-items: center;
    justify-content: center;
  }
  .band-url {
    color: var(--band-text);
    font-size: 21px;
    font-weight: 700;
    letter-spacing: 0.5px;
  }

  .back-brand {
    position: absolute;
    top: 50%; left: 50%;
    transform: translate(-50%, -50%) rotate(90deg);
    white-space: nowrap;
    display: flex;
    align-items: center;
    gap: 14px;
    color: var(--gold);
    font-size: 52px;
    font-weight: 700;
  }
  .back-brand-dot {
    width: 18px; height: 18px;
    border-radius: 50%;
    background: var(--gold);
  }
</style>
</head>
<body>
  <section class="card card-front" aria-label="Card front">
    <div class="front-brand">Shaker Barons</div>
    <div class="front-person">
      <div class="person-name">Elliot</div>
      <div class="person-role">Owner</div>
    </div>
    <div class="front-contacts">
      <div>0491 556 203</div>
      <div>0478 330 914</div>
      <div>info@shakerbarons.net</div>
      <div>Po Box 5821 Marlow</div>
      <div>Queensland, Australia</div>
    </div>
    <div class="front-band">
      <span class="band-url">www.shakerbarons.net</span>
    </div>
  </section>

  <section class="card card-back" aria-label="Card back">
    <div class="back-brand">
      <span class="back-brand-name">Shaker Barons</span>
      <span class="back-brand-dot"></span>
    </div>
  </section>
</body>
</html>
```